NZ First of it's kind solutions directory and marketplace for busy Mums needs a business card design

We need a business card design for our new nationwide business in NZ (long term plans to go global). We provide solutions to the everyday challenges that busy Mums face by connecting them with quality communities and suppliers of carefully selected, relevant products and services. We sell direct via our online marketplace. The final design should communicate our values of inclusivity, quality and smart solutions. Colours should incorporate our logo colour palette of #477077 and #6ba8b2. Our website is at https://www.brightnestly.com

Target Market(s)

busy Mums, Age 28 – 50, female, income over $100K, location main centres NZ primarily but NZ wide. Is likely juggling work or career with a young family. Probably had hobbies which have fallen by the wayside.
-Wants to succeed in her chosen career without compromising on family life
-to successfully juggle her career without feeling like she is compromising her children
- Is time poor, something always has to give and it’s generally her health (she’ll stay up late, get stressed)
- probably ex corporate or professional career. Has discretional income

Industry/Entity Type

Business

Contact Information for Business Card

Jodie Farnsworth, Founder, BrightNestly.com (Strapline Browse; Pick; Sorted), 48 Kowhai Terrace, Hillsborough, Auckland 1058, New Zealand. Mob: 021 437 518 Ph: +64 (0)9 584 7163

Font styles to use
Other font styles liked:
• Raleway, and/or Architects Daughter

Colors
00a990
33b8a4
86cfc6
cfeae6

Requirements
Must have
• the above details, streamline. the logo and colours associated with those logos
Should not have
• foil or metallic colours

```html
<!DOCTYPE html>
<html lang="en">
<head>
<meta charset="utf-8">
<title>BrightNestly Business Card</title>
<link rel="stylesheet" href="https://fonts.googleapis.com/css2?family=Raleway:wght@400;500;600;700;800&display=swap">
<style>
  :root {
    --teal-dark: #4a7079;
    --teal-brand: #477077;
    --teal-light: #6ba8b2;
    --ink: #4a4a4a;
    --paper: #ffffff;
    --stage: #2b2b2b;
  }
  * { box-sizing: border-box; margin: 0; padding: 0; }
  html, body {
    width: 1189px; height: 1200px; overflow: hidden;
    background: var(--stage);
    font-family: "Raleway", sans-serif;
  }
  .card {
    position: absolute; left: 166px;
    width: 856px; height: 490px;
    overflow: hidden;
  }
  .card--front { top: 66px; background: var(--teal-dark); }
  .card--back { top: 625px; background: var(--paper); }

  /* front */
  .front-brand {
    position: absolute; left: 0; right: 0; top: 272px;
    display: flex; align-items: center; justify-content: center; gap: 16px;
  }
  .brand-dot {
    width: 44px; height: 44px; border-radius: 50%;
    background: var(--paper);
  }
  .front-brand .brand-name {
    color: var(--paper); font-weight: 800; font-size: 58px; letter-spacing: -1px;
    line-height: 1;
  }
  .front-url {
    position: absolute; left: 0; right: 0; top: 351px;
    text-align: center; color: var(--paper);
    font-size: 18px; letter-spacing: 3px; font-weight: 400;
  }
  .front-url strong { font-weight: 700; }

  /* back */
  .back-band {
    position: absolute; left: 0; top: 0; bottom: 0; width: 98px;
    background: var(--teal-dark);
  }
  .back-brand {
    position: absolute; left: 134px; top: 86px;
    display: flex; align-items: center; gap: 14px;
  }
  .back-brand .brand-dot { width: 40px; height: 40px; background: var(--teal-brand); }
  .back-brand .brand-name {
    color: var(--teal-brand); font-weight: 800; font-size: 48px; letter-spacing: -1px;
    line-height: 1;
  }
  .person {
    position: absolute; left: 139px; top: 294px;
  }
  .person-name {
    font-size: 26px; font-weight: 700; letter-spacing: -0.5px; line-height: 1;
    color: var(--teal-brand);
  }
  .person-name .surname { color: var(--teal-light); font-weight: 600; }
  .person-role {
    font-size: 19px; color: var(--ink); margin-top: 2px;
  }
  .rule {
    position: absolute; left: 232px; width: 581px; top: 339px;
    height: 1.5px; background: var(--teal-light);
  }
  .contacts {
    position: absolute; left: 139px; top: 378px;
    list-style: none;
  }
  .contacts li {
    display: flex; align-items: center; gap: 9px;
    height: 27px; font-size: 20px; color: var(--ink);
  }
  .contacts svg { width: 22px; height: 22px; flex: none; }
  .address {
    position: absolute; left: 478px; top: 378px;
    font-style: normal; font-size: 20px; line-height: 27px; color: var(--ink);
  }
</style>
</head>
<body>
  <section class="card card--front">
    <div class="front-brand">
      <span class="brand-dot"></span>
      <span class="brand-name">BrightNestly</span>
    </div>
    <p class="front-url">www.<strong>brightnestly</strong>.com</p>
  </section>

  <section class="card card--back">
    <div class="back-band"></div>
    <div class="back-brand">
      <span class="brand-dot"></span>
      <span class="brand-name">BrightNestly</span>
    </div>

    <div class="person">
      <p class="person-name">Jodie <span class="surname">Farnsworth</span></p>
      <p class="person-role">Founder</p>
    </div>
    <div class="rule"></div>

    <ul class="contacts">
      <li>
        <svg viewBox="0 0 22 22" aria-hidden="true"><circle cx="11" cy="11" r="10" fill="none" stroke="#6ba8b2" stroke-width="1.4"/><rect x="7.5" y="5.5" width="7" height="11" rx="1.2" fill="none" stroke="#6ba8b2" stroke-width="1.3"/></svg>
        021 437 518
      </li>
      <li>
        <svg viewBox="0 0 22 22" aria-hidden="true"><circle cx="11" cy="11" r="10" fill="none" stroke="#6ba8b2" stroke-width="1.4"/><path d="M6 9.5c0-2 10-2 10 0v1h-2.5v-1h-5v1H6z" fill="#6ba8b2"/><rect x="7.5" y="11" width="7" height="4.5" rx="1" fill="#6ba8b2"/></svg>
        +64 (0)9 584 7163
      </li>
      <li>
        <svg viewBox="0 0 22 22" aria-hidden="true"><circle cx="11" cy="11" r="10" fill="none" stroke="#6ba8b2" stroke-width="1.4"/><circle cx="11" cy="11" r="6" fill="none" stroke="#6ba8b2" stroke-width="1.1"/><ellipse cx="11" cy="11" rx="2.6" ry="6" fill="none" stroke="#6ba8b2" stroke-width="1"/><path d="M5 11h12M6 8h10M6 14h10" stroke="#6ba8b2" stroke-width="0.9"/></svg>
        www.brightnestly.com
      </li>
    </ul>

    <address class="address">
      48 Kowhai Terrace,<br>
      Hillsborough, Auckland 1058<br>
      New Zealand
    </address>
  </section>
</body>
</html>
```